Design a Logo and Business Card

Please see the requirements here:
https://www.filevault-example.net/s/q7kx2mtrwplz9ab/Requirements.pdf?dl=0
Leave a comment if you have any questions.

```html
<!DOCTYPE html>
<html lang="en">
<head>
<meta charset="utf-8">
<title>Brightwall Painting – Business Card</title>
<link rel="stylesheet" href="https://fonts.googleapis.com/css2?family=Montserrat:wght@400;500;700;800&display=swap">
<style>
  :root {
    --page: #e6e4e1;
    --card-light: #f7f7f5;
    --card-dark: #262626;
    --card-dark-edge: #1a1a1a;
    --ink: #1e1e1e;
    --ink-soft: #3a3a3a;
    --paper-text: #f2f2f2;
    --accent: #d8262f;
    --rule-light: #2a2a2a;
    --rule-dark: #d9d9d9;
  }
  * { box-sizing: border-box; margin: 0; padding: 0; }
  html, body {
    width: 796px; height: 1200px; overflow: hidden;
    background: var(--page);
    font-family: "Montserrat", sans-serif;
  }
  .sheet { position: relative; width: 796px; height: 1200px; }
  .card {
    position: absolute; left: 78px; width: 640px; height: 366px;
    border-radius: 26px; overflow: hidden;
    box-shadow: 0 10px 24px rgba(0,0,0,0.18);
  }
  .card--front { top: 170px; background: var(--card-light); color: var(--ink); }
  .card--back {
    top: 640px;
    background: linear-gradient(160deg, #3a3a3a 0%, var(--card-dark) 45%, var(--card-dark-edge) 100%);
    color: var(--paper-text);
  }

  .brand {
    position: absolute; display: flex; align-items: center; gap: 10px;
    font-weight: 800; text-transform: uppercase; letter-spacing: 0.5px;
    white-space: nowrap;
  }
  .brand__mark { background: var(--accent); flex: none; }
  .card--front .brand { left: 34px; top: 32px; font-size: 24px; color: var(--ink); }
  .card--front .brand__mark { width: 18px; height: 18px; }
  .card--back .brand {
    left: 0; right: 0; top: 140px; justify-content: center;
    font-size: 40px; color: var(--paper-text);
  }
  .card--back .brand__mark { width: 30px; height: 30px; }

  .contact { position: absolute; right: 36px; top: 120px; text-align: right; }
  .contact__name { font-size: 27px; font-weight: 700; letter-spacing: 0.3px; }
  .contact__company { font-size: 14px; color: var(--ink-soft); margin-top: 2px; }
  .contact__line {
    display: flex; justify-content: flex-end; align-items: center; gap: 10px;
    font-size: 14px; color: var(--ink-soft); margin-top: 10px;
  }
  .contact__line:first-of-type { margin-top: 18px; }
  .contact__icon { width: 16px; height: 16px; flex: none; }

  /* service line: text and rule share one row so they never overlap */
  .service-row {
    position: absolute; display: flex; align-items: center; gap: 18px;
  }
  .service-row__text { font-size: 15px; font-weight: 500; white-space: nowrap; flex: none; }
  .service-row__rule { flex: 1; height: 1px; }

  .card--front .service-row { left: 34px; right: 0; top: 268px; }
  .card--front .service-row__text { color: var(--ink-soft); }
  .card--front .service-row__rule { background: var(--rule-light); }

  .card--back .service-row { left: 20px; right: 34px; top: 290px; flex-direction: row; }
  .card--back .service-row__text { color: var(--paper-text); }
  .card--back .service-row__rule { background: var(--rule-dark); opacity: 0.7; }

  .card--back .rule-side {
    position: absolute; left: 20px; top: 60px; width: 1px; height: 180px;
    background: var(--rule-dark); opacity: 0.7;
  }
</style>
</head>
<body>
<main class="sheet">

  <section class="card card--front" aria-label="Business card front">
    <div class="brand"><span class="brand__mark"></span>Brightwall Painting</div>

    <div class="contact">
      <div class="contact__name">Dana Reyes</div>
      <div class="contact__company">Brightwall Painting</div>
      <div class="contact__line">
        (617) 555 - 0142
        <svg class="contact__icon" viewBox="0 0 16 16" aria-hidden="true">
          <rect x="4" y="1.5" width="8" height="13" rx="1.5" fill="none" stroke="#d8262f" stroke-width="1.6"/>
        </svg>
      </div>
      <div class="contact__line">
        hello@brightwall.net
        <svg class="contact__icon" viewBox="0 0 16 16" aria-hidden="true">
          <rect x="1.5" y="3.5" width="13" height="9" fill="none" stroke="#d8262f" stroke-width="1.6"/>
          <path d="M1.5 3.5 L8 9 L14.5 3.5" fill="none" stroke="#d8262f" stroke-width="1.6"/>
        </svg>
      </div>
    </div>

    <div class="service-row">
      <span class="service-row__text">Residential &amp; Commercial</span>
      <span class="service-row__rule"></span>
    </div>
  </section>

  <section class="card card--back" aria-label="Business card back">
    <div class="rule-side"></div>
    <div class="brand"><span class="brand__mark"></span>Brightwall Painting</div>
    <div class="service-row">
      <span class="service-row__rule"></span>
      <span class="service-row__text">Interior - Exterior &amp; Pos Cleaning Services</span>
    </div>
  </section>

</main>
</body>
</html>
```